Stationary for Hair Cosmetic company

We mainly sell hair thickening products www.morvello-wellform.de/morvello-hair/ Hair thickening products are a smart and easy solution for thinning hair for both men and women. We sell very information oriented in an honest undramatic manner.

We would like to see a decent color and style that is suitable for men and women. It shall be rather modern with a vintage spin as our own product (Morvello Bottle). Please use our logo (attatched).

Please bias your design to the bottle. To give you an idea: Chalk design like http://de.pixaverum.com/id/48213597 or one-color watercolor like http://de.pixaverum.com/id/63925180 is appreciated but not necessary.

Good but rejected designs will get compensation.

Target Market(s)

Wide range in demographics: age 20-55; 45% male, 55% women; issues with hair loss; self-conscious

Industry/Entity Type

Hair

Colors
3377b5
33a6d7
32b7a4
cbdf83
fbf289
fee18a
f9bb93
f05157

Requirements
Must have
• trustworthiness
Nice to have
• Chalk design like http://de.pixaverum.com/id/48213597 or one-color watercolor like http://de.pixaverum.com/id/63925180 is appreciated but not necessary

```html
<!DOCTYPE html>
<html lang="en">
<head>
<meta charset="utf-8">
<title>Morvello Hair – Stationery</title>
<link href="https://fonts.googleapis.com/css2?family=Marcellus+SC&family=Open+Sans:wght@400;600&display=swap" rel="stylesheet">
<style>
  :root {
    --backdrop: #e3e4e6;
    --paper: #ffffff;
    --charcoal: #444546;
    --charcoal-deep: #363738;
    --charcoal-soft: #58595a;
    --ink: #2b2b2b;
    --muted: #6d6e70;
    --rule: #9a9b9d;
    --faint: #f1f1f1;
    --accent-dot: #e0524f;
    --shadow: 0 3px 8px rgba(0,0,0,.22);
  }
  * { box-sizing: border-box; margin: 0; padding: 0; }
  html, body { width: 1200px; height: 640px; overflow: hidden; }
  body {
    position: relative;
    background: var(--backdrop);
    font-family: "Open Sans", Arial, sans-serif;
    color: var(--ink);
  }
  .wordmark {
    font-family: "Marcellus SC", Georgia, serif;
    font-weight: 400;
    letter-spacing: .06em;
    white-space: nowrap;
  }
  .mark-dot { border-radius: 50%; display: block; }

  /* Letterhead */
  .letterhead {
    position: absolute; left: 34px; top: 16px; width: 310px; height: 438px;
    background: var(--paper); box-shadow: var(--shadow);
  }
  .letterhead .brand { position: absolute; left: 28px; top: 14px; text-align: center; width: 70px; }
  .letterhead .mark-dot { width: 34px; height: 40px; border: 2px solid var(--ink); margin: 0 auto 6px; border-radius: 50%; }
  .letterhead .wordmark { font-size: 9.5px; color: var(--ink); }
  .letterhead .rule {
    position: absolute; left: 98px; right: 0; top: 93px; height: 1px; background: var(--rule);
  }
  .letterhead .contact { position: absolute; left: 216px; top: 37px; font-size: 4.6px; line-height: 8px; color: var(--ink); }
  .contact-row { display: flex; align-items: center; gap: 3px; }
  .contact-row svg { flex: none; }
  .letterhead .address { margin-top: 1px; line-height: 6px; }
  .letterhead .watermark {
    position: absolute; left: 152px; top: 212px; width: 150px; height: 200px; border-radius: 50%;
    background: radial-gradient(ellipse at center, #f4f4f4 0%, var(--faint) 60%, #f7f7f7 100%);
  }

  /* Business cards */
  .card {
    position: absolute; top: 484px; width: 215px; height: 130px; box-shadow: var(--shadow);
  }
  .card-front { left: 34px; background: var(--charcoal); color: #fff; }
  .card-front .brand-panel {
    position: absolute; left: 10px; top: 10px; width: 84px; height: 110px; border-radius: 50%;
    background: var(--paper); display: flex; flex-direction: column; align-items: center; justify-content: center; gap: 6px;
  }
  .card-front .mark-dot { width: 18px; height: 18px; background: var(--charcoal); }
  .card-front .brand-panel .wordmark { font-size: 9px; color: var(--ink); letter-spacing: .03em; }
  .card-front .person { position: absolute; left: 114px; top: 27px; }
  .card-front .person-name { font-family: "Marcellus SC", Georgia, serif; font-size: 10px; letter-spacing: .05em; }
  .card-front .person-role { font-size: 5.5px; color: #d8d8d8; margin-top: 1px; }
  .card-front .details { position: absolute; left: 114px; top: 80px; font-size: 6px; line-height: 9.2px; color: #eee; }
  .card-back { left: 261px; background: var(--paper); }
  .card-back .brand { position: absolute; inset: 0; display: flex; flex-direction: column; align-items: center; justify-content: center; gap: 10px; }
  .card-back .mark-dot { width: 42px; height: 52px; background: var(--ink); border-radius: 50%; }
  .card-back .wordmark { font-size: 12px; color: var(--ink); }

  /* Folder (opened flat) */
  .folder {
    position: absolute; left: 436px; top: 36px; width: 464px; height: 300px;
    display: flex; box-shadow: var(--shadow);
  }
  .folder-panel { position: relative; width: 232px; height: 300px; overflow: hidden; }
  .pattern-fill {
    position: absolute; inset: 0;
    background: linear-gradient(160deg, var(--charcoal-soft) 0%, var(--charcoal) 45%, var(--charcoal-deep) 100%);
  }
  .folder-back { border-right: 1px solid #2e2f30; }
  .folder-back .seal {
    position: absolute; left: 84px; top: 214px; width: 34px; height: 42px; border-radius: 50%;
    background: var(--paper); display: flex; align-items: center; justify-content: center;
  }
  .folder-back .seal .mark-dot { width: 10px; height: 10px; background: var(--charcoal); }
  .folder-back .footer-contacts {
    position: absolute; left: 48px; bottom: 12px; display: flex; gap: 7px; font-size: 3.4px; color: #ddd;
  }
  .footer-contacts span { display: flex; align-items: center; gap: 2px; }
  .footer-contacts i { width: 4px; height: 4px; border-radius: 50%; background: var(--accent-dot); display: block; }

  .brand-badge { position: absolute; display: flex; flex-direction: column; align-items: center; gap: 4px; }
  .brand-badge .mark-dot { background: var(--paper); }
  .brand-badge .wordmark { color: #fff; }
  .folder-front .brand-badge { right: 14px; top: 14px; }
  .folder-front .brand-badge .mark-dot { width: 30px; height: 36px; }
  .folder-front .brand-badge .wordmark { font-size: 7.5px; }

  .title-band {
    position: absolute; left: 0; right: 0; background: var(--paper); text-align: center;
    font-family: "Marcellus SC", Georgia, serif; color: var(--ink); letter-spacing: .04em;
  }
  .title-band .kicker { display: block; }
  .title-band .headline { display: block; font-weight: 400; }
  .folder-front .title-band { top: 155px; height: 36px; padding-top: 5px; }
  .folder-front .kicker { font-size: 9.5px; line-height: 11px; }
  .folder-front .headline { font-size: 13px; line-height: 15px; }

  /* Brochure */
  .brochure {
    position: absolute; left: 926px; top: 248px; width: 244px; height: 350px;
    overflow: hidden; box-shadow: 0 4px 10px rgba(0,0,0,.28);
  }
  .brochure .brand-badge { right: 16px; top: 16px; }
  .brochure .brand-badge .mark-dot { width: 38px; height: 46px; }
  .brochure .brand-badge .wordmark { font-size: 9px; }
  .brochure .title-band { top: 148px; height: 46px; padding-top: 7px; }
  .brochure .kicker { font-size: 12px; line-height: 13px; }
  .brochure .headline { font-size: 16px; line-height: 19px; }
</style>
</head>
<body>

  <!-- Letterhead -->
  <section class="letterhead" aria-label="Letterhead">
    <div class="brand">
      <span class="mark-dot"></span>
      <span class="wordmark">Morvello Hair</span>
    </div>
    <address class="contact" style="font-style:normal">
      <div class="contact-row">
        <svg width="5" height="5" viewBox="0 0 10 10"><circle cx="5" cy="5" r="5" fill="#2b2b2b"/><path d="M3.3 2.6l1 1-.5.7a4 4 0 0 0 1.9 1.9l.7-.5 1 1-.7.8C5 7.4 2.6 5 2.5 3.3z" fill="#fff"/></svg>
        041 555 2093
      </div>
      <div class="contact-row">
        <svg width="5" height="5" viewBox="0 0 10 10"><circle cx="5" cy="5" r="5" fill="#2b2b2b"/><path d="M3.3 2.6l1 1-.5.7a4 4 0 0 0 1.9 1.9l.7-.5 1 1-.7.8C5 7.4 2.6 5 2.5 3.3z" fill="#fff"/></svg>
        041 555 2094
      </div>
      <div class="contact-row">
        <svg width="5" height="5" viewBox="0 0 10 10"><circle cx="5" cy="5" r="5" fill="#2b2b2b"/><rect x="2.6" y="3.3" width="4.8" height="3.4" fill="none" stroke="#fff" stroke-width=".8"/><path d="M2.6 3.3L5 5.2l2.4-1.9" fill="none" stroke="#fff" stroke-width=".8"/></svg>
        hello@morvellomail.com
      </div>
      <div class="address">Addressline PO Box 1850, City Name<br>Harwick Lane, Country Name</div>
    </address>
    <div class="rule"></div>
    <div class="watermark" role="img" aria-label="Faint engraved hair-wave emblem in light grey"></div>
  </section>

  <!-- Business card front -->
  <section class="card card-front" aria-label="Business card front">
    <div class="brand-panel">
      <span class="mark-dot"></span>
      <span class="wordmark">Morvello Hair</span>
    </div>
    <div class="person">
      <div class="person-name">Corin Aldaway</div>
      <div class="person-role">Director</div>
    </div>
    <div class="details">
      <div class="contact-row">
        <svg width="6" height="6" viewBox="0 0 10 10"><circle cx="5" cy="5" r="5" fill="#ddd"/><rect x="3.4" y="2.2" width="3.2" height="5.6" rx=".6" fill="#444"/></svg>
        05550198734
      </div>
      <div class="contact-row">
        <svg width="6" height="6" viewBox="0 0 10 10"><circle cx="5" cy="5" r="5" fill="#ddd"/><path d="M3.3 2.6l1 1-.5.7a4 4 0 0 0 1.9 1.9l.7-.5 1 1-.7.8C5 7.4 2.6 5 2.5 3.3z" fill="#444"/></svg>
        05550198735
      </div>
      <div class="contact-row">
        <svg width="6" height="6" viewBox="0 0 10 10"><circle cx="5" cy="5" r="5" fill="#ddd"/><rect x="2.6" y="3.3" width="4.8" height="3.4" fill="none" stroke="#444" stroke-width=".8"/><path d="M2.6 3.3L5 5.2l2.4-1.9" fill="none" stroke="#444" stroke-width=".8"/></svg>
        info@morvellomail.com
      </div>
      <div class="contact-row">
        <svg width="6" height="6" viewBox="0 0 10 10"><circle cx="5" cy="5" r="5" fill="#ddd"/><circle cx="5" cy="5" r="2.6" fill="none" stroke="#444" stroke-width=".7"/><path d="M2.4 5h5.2M5 2.4v5.2" stroke="#444" stroke-width=".6"/></svg>
        www.morvellohair.com
      </div>
    </div>
  </section>

  <!-- Business card back -->
  <section class="card card-back" aria-label="Business card back">
    <div class="brand">
      <span class="mark-dot"></span>
      <span class="wordmark">Morvello Hair</span>
    </div>
  </section>

  <!-- Presentation folder, opened flat -->
  <section class="folder" aria-label="Presentation folder">
    <div class="folder-panel folder-back">
      <div class="pattern-fill" role="img" aria-label="Dark charcoal engraved hair-wave pattern with large initial letter"></div>
      <div class="seal"><span class="mark-dot"></span></div>
      <div class="footer-contacts">
        <span><i></i>041 555 2093</span>
        <span><i></i>hello@morvellomail.com</span>
        <span><i></i>12 Elm Row, Harwick</span>
      </div>
    </div>
    <div class="folder-panel folder-front">
      <div class="pattern-fill" role="img" aria-label="Dark charcoal engraved hair-wave pattern with large initial letter"></div>
      <div class="brand-badge">
        <span class="mark-dot"></span>
        <span class="wordmark">Morvello Hair</span>
      </div>
      <div class="title-band">
        <span class="kicker">How To Repair</span>
        <span class="headline">Your Hair</span>
      </div>
    </div>
  </section>

  <!-- Brochure cover -->
  <section class="brochure" aria-label="Brochure cover">
    <div class="pattern-fill" role="img" aria-label="Dark charcoal engraved hair-wave pattern with large initial letter"></div>
    <div class="brand-badge">
      <span class="mark-dot"></span>
      <span class="wordmark">Morvello Hair</span>
    </div>
    <div class="title-band">
      <span class="kicker">How To Repair</span>
      <span class="headline">Your Hair</span>
    </div>
  </section>

</body>
</html>
```